Dentist Home Page Design

We need a home page design to be used as a responsive wordpress theme for our dentist website. Website overall look and feel should look professional, yet very friendly as going to dentist is not people's favorite thing to do, for most it might even be scary. We want our website to differentiate with its design from all other generic looking cookie cutter dentists and creates a branded feel.
you can use a generic image for the 680x300px banner on the home pageif you like in the meantime). Total width should not exceed 960 px
Please follow the layout on the wireframes, do not add or delete random elements.
Target Market(s)
mostly targets male/female between 30-45, families with kids as well.
Industry/Entity Type
It Professional
Colors
Designer to choose colors to be used in the design.
Look and feel
Each slider illustrates characteristics of the customer's brand and the style your logo design should communicate.

```html
<!DOCTYPE html>
<html lang="en">
<head>
<meta charset="utf-8">
<title>Harbor Dental – Home</title>
<link href="https://fonts.googleapis.com/css2?family=Open+Sans:wght@400;600;700&family=Cabin:wght@400&display=swap" rel="stylesheet">
<style>
:root{
  --cyan:#1ba6dc;
  --pink:#e0306f;
  --dark:#323234;
  --nav:#3a3a3c;
  --text:#8a8a8a;
  --heading:#2d2d2d;
  --rule:#e3e3e3;
  --red:#b3171b;
  --field:#fff;
  --footer-field:#404044;
  --brand:#4a4a4c;
}
*{margin:0;padding:0;box-sizing:border-box}
html,body{width:684px;height:1200px;overflow:hidden;background:#fff}
body{position:relative;font-family:"Open Sans",Arial,sans-serif;color:var(--text);font-size:7px}
.abs{position:absolute}
.top-strip{left:0;top:0;width:684px;height:3px;background:var(--dark)}
/* header */
.brand{left:92px;top:31px;font-size:15px;font-weight:600;color:var(--brand);line-height:20px;white-space:nowrap}
.doctor-mark{left:218px;top:29px;font-size:10px;font-weight:600;color:#6d6d6d;line-height:12px;white-space:nowrap}
.doctor-mark small{display:block;font-size:5px;font-weight:400;color:#9a9a9a;margin-top:2px}
.socials{left:509px;top:21px;display:flex;gap:5px}
.socials span{width:15px;height:15px;border-radius:50%;background:#c9c9c9}
.call{left:468px;top:46px;font-size:7px;color:var(--cyan);white-space:nowrap}
.call b{font-size:13px;color:var(--pink);font-weight:600;margin-left:3px;vertical-align:-2px}
/* nav */
.nav{left:77px;top:77px;width:527px;height:20px;background:var(--nav);display:flex;align-items:center;padding-left:17px}
.nav a{color:#fff;text-decoration:none;font-size:6.6px;margin-right:18.5px;line-height:20px;white-space:nowrap}
.nav a.active{background:var(--cyan);padding:0 5px;margin-left:-5px}
/* banner */
.banner{left:77px;top:97px;width:527px;height:146px;background:linear-gradient(90deg,#d6c0b4 0%,#8a5a45 30%,#6a3e2c 55%,#c08a6c 80%,#e9c4a4 100%)}
.consult{left:415px;top:97px;width:189px;height:146px;background:rgba(245,210,185,.55)}
.consult h2{height:26px;background:var(--cyan);color:#fff;font-size:10.5px;font-weight:400;line-height:26px;padding-left:37px;position:relative}
.consult h2 svg{position:absolute;left:17px;top:7px}
.field{position:absolute;height:18px;background:var(--field);opacity:.93;font-size:6px;color:#999;line-height:18px;padding-left:5px;border:1px solid #f0d8c8}
.submit{left:543px;top:225px;font-size:9px;color:var(--cyan);display:flex;align-items:center;gap:4px}
.submit i{width:10px;height:10px;border-radius:50%;background:var(--cyan);display:inline-block;position:relative}
/* sections */
.sec-title{font-size:6.4px;font-weight:700;color:var(--heading);display:flex;align-items:center;gap:8px;white-space:nowrap}
.sec-title::after{content:"";flex:1;height:1px;background:var(--rule)}
.copy{font-size:6.6px;line-height:11.4px;text-align:justify;color:var(--text)}
.copy a{color:var(--cyan);font-style:italic;text-decoration:none}
.video{left:438px;top:299px;width:166px;height:134px;border-top:4px solid var(--cyan);background:linear-gradient(135deg,#9fd0ea,#e7c7c0 60%,#b5d6ea)}
.play{left:502px;top:354px}
.services{left:77px;top:488px;width:166px;display:grid;grid-template-columns:83px 83px;row-gap:5.6px;font-family:"Cabin",sans-serif;font-size:8px;line-height:12px;color:#707070}
.more{left:175px;top:601px;font-size:6.6px;color:var(--cyan);font-style:italic;display:flex;align-items:center;gap:6px}
.plus{width:11px;height:11px;background:var(--cyan);position:relative;display:inline-block}
.plus::before,.plus::after{content:"";position:absolute;background:#fff;left:50%;top:20%;width:1.4px;height:60%;margin-left:-.7px}
.plus::after{left:20%;top:50%;width:60%;height:1.4px;margin-left:0;margin-top:-.7px}
.caption{font-size:6.6px;line-height:11.4px;color:var(--text)}
.thumb{width:60px;height:43px;border:1px solid #444}
.thumb-label{font-size:6px;color:#333;text-align:center;width:60px;margin-top:3px}
.arrows{left:586px;top:634px;display:flex;gap:1px}
.arrows span{width:9px;height:9px;border-radius:50%;background:var(--dark);position:relative}
.case-img{width:166px;height:88px;border-bottom:4px solid var(--cyan)}
.case-title{font-size:9px;color:#333}
.case-text{font-size:6.6px;line-height:10px;color:var(--text)}
.fans{left:88px;top:836px;font-size:6px;color:#333}
.fans b{color:#3b5998;font-weight:600}
.fan-row{left:88px;top:852px;display:flex}
.fan-row span{width:25px;height:23px;background:linear-gradient(160deg,#c9a48c,#4a4a52)}
.fan-row span:nth-child(even){background:linear-gradient(160deg,#8e7f76,#2e2e34)}
.follow{left:495px;top:853px;width:96px;height:20px;background:var(--cyan);color:#fff;font-size:7.4px;line-height:20px;text-align:center}
.divider{left:77px;top:892px;width:527px;height:1px;background:var(--rule)}
/* footer */
.footer{left:77px;top:920px;width:527px;height:260px;background:var(--dark);color:#a5a5a5;font-size:6.6px}
.footer h4{font-size:6.6px;color:#fff;font-weight:700;position:absolute;white-space:nowrap}
.footer p{position:absolute;line-height:11.6px}
.footer u{color:#a5a5a5}
.hours{position:absolute;left:37px;top:116px;border-collapse:collapse}
.hours td{line-height:12.4px;padding:0;font-size:6.6px;color:#a5a5a5}
.hours td:first-child{width:50px}
.map{position:absolute;left:187px;top:87px;width:155px;height:151px;background:linear-gradient(135deg,#dfe8d4,#f3eee2 45%,#c8dcec)}
.nl-field{position:absolute;left:376px;width:115px;height:19px;background:var(--footer-field);color:#a5a5a5;font-size:6.2px;line-height:19px;padding-left:6px}
.signup-btn{position:absolute;left:430px;top:177px;width:58px;height:20px;background:var(--red);color:#fff;font-size:6.6px;font-weight:700;line-height:20px;text-align:center}
.bottom{left:0;top:1180px;width:684px;height:20px;background:var(--dark);font-size:6.6px;color:#a5a5a5;line-height:20px}
.bottom b{color:#fff;font-weight:400}
</style>
</head>
<body>
<div class="abs top-strip"></div>

<header>
  <div class="abs brand">Harbor Dental</div>
  <div class="abs doctor-mark">Dr. Martin Kovar<small>General Dental · Orthodontics for Adults &amp; Children</small></div>
  <div class="abs socials" aria-label="Social links"><span></span><span></span><span></span><span></span><span></span></div>
  <div class="abs call">Click to Call <b>(555) 210-4477</b></div>
</header>

<nav class="abs nav">
  <a class="active">HOME</a><a>ABOUT US</a><a>OUR SERVICES</a><a>OUR TECHNOLOGY</a><a>DENTAL CARE</a><a>CASE STUDIES</a><a>NEW PATIENTS</a><a>CONTACT US</a>
</nav>

<div class="abs banner" role="img" aria-label="Banner photo of smiling patients"></div>
<form class="abs consult">
  <h2><svg width="12" height="13" viewBox="0 0 12 13"><path d="M2 1c2-1 3 1 4 1s2-2 4-1 1 5 0 7-1 5-2 5-1-4-2-4-1 4-2 4-1-3-2-5S0 2 2 1z" fill="#fff"/></svg>Request a Free Consultation</h2>
  <div class="field" style="left:12px;top:34px;width:164px">Your Full Name</div>
  <div class="field" style="left:12px;top:57px;width:164px">Your Phone Number</div>
  <div class="field" style="left:12px;top:80px;width:164px">Your Best Email</div>
  <div class="field" style="left:12px;top:103px;width:80px">Preferred Date</div>
  <div class="field" style="left:96px;top:103px;width:80px">Preferred Time</div>
</form>
<div class="abs submit">Submit <i><svg width="10" height="10" viewBox="0 0 10 10"><path d="M4 3l2 2-2 2" stroke="#fff" stroke-width="1.3" fill="none"/></svg></i></div>

<section>
  <h3 class="abs sec-title" style="left:77px;top:274px;width:346px">YOUR EXPERIENCE IN DENTISTY BEGINS NOW!</h3>
  <p class="abs copy" style="left:77px;top:296px;width:165px">Welcome to Harbor Dental! We are glad of your visit. Whether you are a new patient looking around for a dentist or an existing patient searching for information, we want you to know that we strive to understand the unique needs and desires of each individual patient so that a tailored and customized approach to treatment can be prescribed. At Harbor Dental, we not only treat teeth, we treat people.<br>Our philosophy is to provide you with holistic, comprehensive care beyond just the treatment of your mouth and teeth. So much in our body is connected</p>
  <p class="abs copy" style="left:258px;top:296px;width:165px">that often treatments to various aliments are temporary solutions and may not get to the root cause of the problem.<br>At Harbor Dental, you can expect a complete oral evaluation supported by dental imaging, a personalized periodontal management program and a well planned course of treatment to perpetuate the long term dental health of patients of all ages. We pledge to provide you, our existing or future patient, a balance of quality, value, personalized care and the latest technology available in dentistry. Every effort has been made to provide you a well &nbsp;&nbsp;&nbsp;<a>read more ...</a></p>

  <h3 class="abs sec-title" style="left:438px;top:274px;width:166px">VIDEO TITLE HERE</h3>
  <div class="abs video" role="img" aria-label="Video still of a dental check-up"></div>
  <svg class="abs play" width="30" height="30" viewBox="0 0 30 30"><circle cx="15" cy="15" r="14" fill="#1ba6dc" stroke="#fff" stroke-width="2"/><path d="M12 9l9 6-9 6z" fill="#fff"/></svg>
</section>

<section>
  <h3 class="abs sec-title" style="left:77px;top:464px;width:166px">OUR DENTAL SERVICES</h3>
  <div class="abs services">
    <span>General Dentistry</span><span>Cosmetic Dentistry</span>
    <span>Braces</span><span>Porcelain Veneers</span>
    <span>Decay Removal</span><span>Dental Implants</span>
    <span>Root Canal</span><span>SnapFit Smile</span>
    <span>Dental Bonding</span><span>UltraThins</span>
    <span>Dental Bridges</span><span>ClearTrays</span>
  </div>
  <div class="abs more">view all services <span class="plus"></span></div>

  <h3 class="abs sec-title" style="left:258px;top:464px;width:165px">DENTISTRY FOR YOUR KIDS</h3>
  <div class="abs" style="left:258px;top:491px;width:165px;height:93px;background:linear-gradient(135deg,#e7d4c8,#bfe0ee 55%,#5fb6dc)" role="img" aria-label="Photo of a child in a dental chair"></div>
  <span class="abs plus" style="left:408px;top:568px;width:15px;height:15px"></span>
  <p class="abs caption" style="left:258px;top:594px;width:165px">We focus entirely on your comfort and convenience.</p>

  <h3 class="abs sec-title" style="left:438px;top:464px;width:166px">MEET DR. MARTIN KOVAR</h3>
  <div class="abs" style="left:438px;top:491px;width:166px;height:93px;background:linear-gradient(135deg,#b39a82,#d8c2ae 50%,#5c6f8a)" role="img" aria-label="Portrait photo of the dentist"></div>
  <span class="abs plus" style="left:589px;top:568px;width:15px;height:15px"></span>
  <p class="abs caption" style="left:438px;top:594px;width:166px">Dr. Martin believes that early intervention is key to oral health and aesthetically pleasing smiles.</p>
</section>

<section>
  <h3 class="abs sec-title" style="left:77px;top:634px;width:166px">EDUCATIONAL VIDEOS</h3>
  <div class="abs" style="left:91px;top:664px"><div class="thumb" style="background:linear-gradient(135deg,#b23a3a,#e6a090)" role="img" aria-label="Video thumbnail: dental implants"></div><div class="thumb-label">Dental Implants</div></div>
  <div class="abs" style="left:168px;top:664px"><div class="thumb" style="background:linear-gradient(135deg,#5a4538,#c4a88a)" role="img" aria-label="Video thumbnail: veneers"></div><div class="thumb-label">Veneers</div></div>
  <div class="abs" style="left:91px;top:729px"><div class="thumb" style="background:linear-gradient(135deg,#7a6d68,#d8d0cc)" role="img" aria-label="Video thumbnail: orthodontics"></div><div class="thumb-label">Orthodontics</div></div>
  <div class="abs" style="left:168px;top:729px"><div class="thumb" style="background:linear-gradient(135deg,#3b8ed0,#f2ece4)" role="img" aria-label="Video thumbnail: snap-fit smile"></div><div class="thumb-label">SnapFit Smile</div></div>

  <h3 class="abs sec-title" style="left:258px;top:634px;width:324px">CASE STUDIES</h3>
  <div class="abs arrows"><span><svg width="9" height="9"><path d="M5 2.5L3 4.5l2 2" stroke="#fff" fill="none"/></svg></span><span><svg width="9" height="9"><path d="M4 2.5l2 2-2 2" stroke="#fff" fill="none"/></svg></span></div>
  <div class="abs case-img" style="left:258px;top:662px;background:linear-gradient(135deg,#f3e6e2,#d27a7c 50%,#f5efec)" role="img" aria-label="Photo of a bright smile"></div>
  <div class="abs case-title" style="left:258px;top:765px">Decay Removal</div>
  <p class="abs case-text" style="left:258px;top:780px;width:166px">Appropriately procrastinate flexible deliverables for interactive initiatives.</p>
  <div class="abs case-img" style="left:438px;top:662px;background:linear-gradient(135deg,#e8b2a8,#f4efea 50%,#d88a86)" role="img" aria-label="Photo of clear aligner trays on teeth"></div>
  <div class="abs case-title" style="left:437px;top:765px">Transparent Braces</div>
  <p class="abs case-text" style="left:438px;top:780px;width:166px">Appropriately procrastinate flexible deliverables for interactive initiatives.</p>
</section>

<section>
  <div class="abs fans"><b>Alex Moreno</b>, <b>Lena Fischer</b> and 2,904,577 others like this.</div>
  <div class="abs fan-row" role="img" aria-label="Row of follower profile pictures"><span></span><span></span><span></span><span></span><span></span><span></span><span></span><span></span><span></span><span></span><span></span><span></span><span></span><span></span><span></span></div>
  <div class="abs follow">Follow Us on Friendbook</div>
  <div class="abs divider"></div>
</section>

<footer class="abs footer">
  <h4 style="left:37px;top:24px">Contact Info &amp; Hours</h4>
  <p style="left:37px;top:42px">Phone: (555) 210-4477<br>Fax: (555) 210-4478<br><u>Email Us</u><br><u>Request Appointment</u></p>
  <h4 style="left:37px;top:100px">Harbor Dental Office Hours</h4>
  <table class="hours">
    <tr><td>Monday:</td><td>12:00 pm &nbsp;- 8:00 pm</td></tr>
    <tr><td>Tuesday:</td><td>10:00 am &nbsp;- 6:00 pm</td></tr>
    <tr><td>Wednesday:</td><td>12:00 pm &nbsp;- 8:00 pm</td></tr>
    <tr><td>Thursday:</td><td>09:00 am &nbsp;- 5:00 pm</td></tr>
    <tr><td>Friday:</td><td>Closed</td></tr>
    <tr><td>Saturday:</td><td>10:00 am &nbsp;- 3:00 pm</td></tr>
    <tr><td>Holidays:</td><td>Closed</td></tr>
  </table>
  <h4 style="left:37px;top:213px">FOLLOW US</h4>
  <p style="left:37px;top:230px">Chirper &nbsp;&nbsp;| &nbsp;&nbsp;Friendbook &nbsp;&nbsp;| &nbsp;&nbsp;Viewtube</p>

  <h4 style="left:187px;top:24px">ADRESS AND DIRECTIONS</h4>
  <p style="left:187px;top:42px"><b style="color:#cfcfcf">Harbor Dental</b><br>1200 Harbor Street East, Lakeview, ON A1B 2C3<br><i>(Free Parking at the Front)</i></p>
  <div class="map" role="img" aria-label="Street map showing the office location"></div>

  <h4 style="left:376px;top:24px">SIGN UP FOR NEWSLETTER</h4>
  <p style="left:376px;top:42px;width:120px">To receive free monthly dental health tips from Dr. Martin Kovar.</p>
  <div class="nl-field" style="top:87px">FIRST NAME</div>
  <div class="nl-field" style="top:113px">EMAIL</div>
  <div class="nl-field" style="top:139px">PHONE</div>
  <div class="signup-btn">SIGN UP</div>
  <h4 style="left:376px;top:213px">USEFUL LINKS</h4>
  <p style="left:376px;top:230px">Terms &nbsp;&nbsp;| &nbsp;&nbsp;Privacy &nbsp;&nbsp;| &nbsp;&nbsp;Sitemap</p>
</footer>

<div class="abs bottom"><span style="position:absolute;left:88px">© 2014 <b>Harbor Dental</b></span><span style="position:absolute;left:536px">All rights reserved.</span></div>
</body>
</html>
```